Car Accessory Flyer to advertise parking sensors, heated seats, car security

I'm looking to have a double sided flyer made that will be distributed locally to advertise heated seats and parking sensors on one side. And trackers and Tarvo immobilisers on the other. Our website is www.dernilo.co.uk
I'm hoping its possible to use wording and pictures from our website.

Target Market(s)
Car owners looking to upgrade their car to have parking sensors or heated seats.
Luxury car owners who are worried about their vehicle being stolen.
Industry/Entity Type
Automotive
Requirements
Must have
- Pictures
Our website, phone number and address
Flyer will be A5 double sided
Nice to have
- A design similar to our website

```html
<!DOCTYPE html>
<html lang="en">
<head>
<meta charset="utf-8">
<title>Dernilo Car Accessory Flyers</title>
<link href="https://fonts.googleapis.com/css2?family=Archivo+Black&family=Barlow+Condensed:wght@300;400;600&display=swap" rel="stylesheet">
<style>
  :root {
    --bg: #b9b3b3;
    --paper: #ffffff;
    --ink: #111111;
    --body: #2a2a2a;
    --green: #4cc497;
    --black: #0b0b0b;
    --charcoal: #3a3a3a;
    --muted-green: #7fd3b3;
    --rule: #222222;
  }
  * { box-sizing: border-box; margin: 0; padding: 0; }
  html, body { width: 1200px; height: 860px; overflow: hidden; }
  body { background: var(--bg); position: relative; font-family: "Barlow Condensed", sans-serif; color: var(--body); }

  .flyer { position: absolute; top: 67px; width: 512px; height: 727px; background: var(--paper); overflow: hidden; }
  .flyer--upgrade { left: 58px; }
  .flyer--security { left: 628px; }

  .hero { position: absolute; left: 0; top: 0; width: 512px; }
  .hero--sensors { height: 231px; background: linear-gradient(160deg, #6e6e6e 0%, #2b2b2b 55%, #1c1c1c 100%); }
  .hero--tracking { height: 300px; background: linear-gradient(180deg, #dfe9f1 0%, #c6d4dc 35%, #7f8c5e 60%, #c9c7b6 100%); }
  .hero-curve { position: absolute; left: 0; top: 0; }

  .headline { position: absolute; left: 0; width: 512px; text-align: center; font-family: "Archivo Black", sans-serif; color: var(--ink); text-transform: uppercase; line-height: 33px; letter-spacing: 0.3px; }
  .flyer--upgrade .headline { top: 243px; font-size: 30px; }
  .flyer--security .headline { top: 280px; font-size: 31px; }

  .tab { position: absolute; height: 21px; background: var(--black); color: var(--green); font-family: "Archivo Black", sans-serif; font-size: 13px; line-height: 21px; text-align: center; letter-spacing: 0.4px;
         clip-path: polygon(0 0, 100% 0, 100% 100%, 0 100%); }
  .tab::after { content: ""; position: absolute; right: 0; top: 0; width: 40px; height: 100%; background: var(--charcoal); clip-path: polygon(60% 0, 100% 0, 100% 100%, 0 100%); z-index: 0; }
  .tab span { position: relative; z-index: 1; }

  .divider { position: absolute; width: 1px; background: var(--rule); }

  .photo { position: absolute; }
  .photo--bumper { background: linear-gradient(160deg, #5a5e63, #3d4146 60%, #8c3a3a); }
  .photo--garage { background: linear-gradient(180deg, #d8d6d0 0%, #3f4650 55%, #6a6a6a 100%); }
  .photo--seat { background: linear-gradient(150deg, #4a4a4a, #161616 60%, #c8232c); }
  .photo--switch { background: linear-gradient(150deg, #2a2a2a, #111 55%, #555); }
  .photo--map { background: linear-gradient(135deg, #eef2ee, #d3e6d0 60%, #e7ecef); border-top: 3px solid #2a4fa3; }
  .photo--keyfob { background: linear-gradient(135deg, #f2f2f2, #2a2a2a 55%, #111); }

  .points { position: absolute; list-style: none; font-size: 10.6px; line-height: 12.3px; font-weight: 300; color: var(--body); }
  .points li { position: relative; padding-left: 15px; margin-bottom: 3.5px; }
  .points li::before { content: ""; position: absolute; left: 0; top: 2px; border-left: 6px solid var(--green); border-top: 3.5px solid transparent; border-bottom: 3.5px solid transparent; }
  .price { position: absolute; color: var(--green); font-weight: 600; font-size: 11px; }

  .footer-band { position: absolute; left: 0; top: 632px; width: 512px; height: 68px; background: var(--charcoal); }
  .footer-band::before { content: ""; position: absolute; left: 0; top: 0; width: 100%; height: 100%; background: var(--black); clip-path: polygon(0 0, 349px 0, 235px 100%, 0 100%); }
  .wordmark { position: absolute; left: 45px; top: 13px; font-family: "Archivo Black", sans-serif; font-size: 37px; line-height: 42px; color: #ffffff; letter-spacing: 1px; }
  .contact { position: absolute; left: 300px; top: 8px; width: 200px; text-align: center; color: var(--muted-green); }
  .contact-lead { font-size: 10px; font-weight: 300; line-height: 12px; }
  .contact-phone { font-size: 21px; font-weight: 300; color: #ffffff; line-height: 24px; display: flex; align-items: center; justify-content: center; gap: 4px; }
  .contact-web { font-size: 13px; font-weight: 300; line-height: 15px; display: flex; align-items: center; justify-content: center; gap: 3px; }

  .address-line { position: absolute; left: 0; top: 704px; width: 512px; display: flex; justify-content: center; align-items: center; gap: 6px; font-size: 10.5px; color: var(--ink); }
  .address-line svg { flex: none; }
</style>
</head>
<body>

<!-- Side one: parking sensors and heated seats -->
<section class="flyer flyer--upgrade">
  <div class="hero hero--sensors" role="img" aria-label="Rear of a silver hatchback with glowing parking sensor waves"></div>

  <h1 class="headline">Upgrade your car<br>with parking sensors<br>or heated seats</h1>

  <div class="tab" style="left:54px; top:353px; width:151px;"><span>PARKING SENSORS</span></div>
  <div class="tab" style="left:307px; top:354px; width:150px;"><span>HEATED SEATS</span></div>
  <div class="divider" style="left:251px; top:354px; height:265px;"></div>

  <div class="photo photo--bumper" style="left:26px; top:387px; width:93px; height:89px;" role="img" aria-label="Rear bumper fitted with parking sensors"></div>
  <div class="photo photo--garage" style="left:136px; top:387px; width:94px; height:89px;" role="img" aria-label="Hatchback in the fitting workshop"></div>
  <div class="photo photo--seat" style="left:272px; top:387px; width:93px; height:89px;" role="img" aria-label="Leather car seat with heated conversion"></div>
  <div class="photo photo--switch" style="left:383px; top:387px; width:93px; height:89px;" role="img" aria-label="Heated seat switch mounted in the interior"></div>

  <ul class="points" style="left:26px; top:491px; width:196px;">
    <li>Make parking a breeze by adding parking sensors to your car.</li>
    <li>We offer a range of different options, our preferred option is flush mount OEM style but have a solution for all vehicles</li>
    <li>Our two most poplar options are the standard “mount from the outside” type and the flush OEM style sensors, both can be colour coded.</li>
  </ul>
  <div class="price" style="left:41px; top:611px;">From £190</div>

  <ul class="points" style="left:272px; top:486px; width:226px;">
    <li>Give yourself the luxury of heated seats.</li>
    <li>We take your ordinary seats and convert them to heated.</li>
    <li>From the outside they will look completely standard, we install heating elements to the base and back between the seat cover and foam, with the addition of a conveniently placed switch with the option of High heat, low heat or off.</li>
    <li>Suitable for both leather and fabric seats.</li>
  </ul>
  <div class="price" style="left:287px; top:609px;">£350 for a pair of front seats</div>

  <footer>
    <div class="footer-band">
      <div class="wordmark">DERNILO</div>
      <div class="contact">
        <div class="contact-lead">for more details call or visit</div>
        <div class="contact-phone">
          <svg width="14" height="14" viewBox="0 0 24 24"><path d="M6.6 10.8a15 15 0 0 0 6.6 6.6l2.2-2.2a1 1 0 0 1 1-.25 11.4 11.4 0 0 0 3.6.6 1 1 0 0 1 1 1V20a1 1 0 0 1-1 1A17 17 0 0 1 3 4a1 1 0 0 1 1-1h3.5a1 1 0 0 1 1 1c0 1.25.2 2.45.6 3.6a1 1 0 0 1-.25 1z" fill="none" stroke="#ffffff" stroke-width="1.8"/></svg>
          0131 555 0192
        </div>
        <div class="contact-web">
          <svg width="10" height="10" viewBox="0 0 24 24"><circle cx="12" cy="12" r="10" fill="none" stroke="currentColor" stroke-width="2"/><path d="M2 12h20M12 2c3 3 3 17 0 20M12 2c-3 3-3 17 0 20" fill="none" stroke="currentColor" stroke-width="2"/></svg>
          www.dernilo.co.uk
        </div>
      </div>
    </div>
    <div class="address-line">
      <svg width="8" height="11" viewBox="0 0 16 22"><path d="M8 1a7 7 0 0 1 7 7c0 5-7 13-7 13S1 13 1 8a7 7 0 0 1 7-7z" fill="none" stroke="var(--green)" stroke-width="2"/><circle cx="8" cy="8" r="2.5" fill="none" stroke="var(--green)" stroke-width="2"/></svg>
      <span>14 Calder Mews, Edinburgh EH11 2QX</span>
      <svg width="12" height="9" viewBox="0 0 24 18" style="margin-left:6px"><rect x="1" y="1" width="22" height="16" fill="none" stroke="var(--green)" stroke-width="2"/><path d="M1 1l11 9 11-9" fill="none" stroke="var(--green)" stroke-width="2"/></svg>
      <span>enquiries@dernilo.co.uk</span>
    </div>
  </footer>
</section>

<!-- Side two: trackers and immobilisers -->
<section class="flyer flyer--security">
  <div class="hero hero--tracking" role="img" aria-label="Hand holding a phone showing a tracking map beside a white convertible on a country road"></div>
  <svg class="hero-curve" width="512" height="300" viewBox="0 0 512 300">
    <path d="M0 320 L0 322 L0 318 C60 270 80 265 130 262 L512 262 L512 300 L0 300 Z" fill="#ffffff"/>
    <path d="M0 322 C30 290 55 268 110 262 L0 262 Z" fill="#ffffff" opacity="0"/>
    <path d="M0 320 C25 290 50 268 100 263 L512 263 L512 300 L0 300 Z" fill="#ffffff"/>
  </svg>

  <h1 class="headline">Worried about your<br>vehicle being stolen<br>track your luxury car</h1>

  <div class="tab" style="left:54px; top:390px; width:150px;"><span>TRACKERS</span></div>
  <div class="tab" style="left:288px; top:391px; width:178px;"><span>AUTOSHIELD TARVO II</span></div>
  <div class="divider" style="left:256px; top:392px; height:230px;"></div>

  <div class="photo photo--map" style="left:33px; top:423px; width:196px; height:111px;" role="img" aria-label="Web tracking dashboard with a street map"></div>
  <div class="photo photo--keyfob" style="left:282px; top:425px; width:191px; height:101px;" role="img" aria-label="Gloved hand taking a car key fob"></div>

  <ul class="points" style="left:26px; top:547px; width:200px;">
    <li>Are you worried about your vehicle being stolen? An insurance approved tracker greatly improves the chance of getting it back. Tracking via and App or web browser. From as little as £399 inc the first year subscription then £100 thereafter.</li>
  </ul>

  <ul class="points" style="left:267px; top:536px; width:222px;">
    <li>The Autoshield Tarvo II helps protect your car against keyless entry theft. Even if a thief has your keys or is using a relay device to program a new key your car will not start unless your unique code has been entered using a combination of buttons on your dash or steering wheel. From £449</li>
  </ul>

  <footer>
    <div class="footer-band">
      <div class="wordmark">DERNILO</div>
      <div class="contact">
        <div class="contact-lead">for more details call or visit</div>
        <div class="contact-phone">
          <svg width="14" height="14" viewBox="0 0 24 24"><path d="M6.6 10.8a15 15 0 0 0 6.6 6.6l2.2-2.2a1 1 0 0 1 1-.25 11.4 11.4 0 0 0 3.6.6 1 1 0 0 1 1 1V20a1 1 0 0 1-1 1A17 17 0 0 1 3 4a1 1 0 0 1 1-1h3.5a1 1 0 0 1 1 1c0 1.25.2 2.45.6 3.6a1 1 0 0 1-.25 1z" fill="none" stroke="#ffffff" stroke-width="1.8"/></svg>
          0131 555 0192
        </div>
        <div class="contact-web">
          <svg width="10" height="10" viewBox="0 0 24 24"><circle cx="12" cy="12" r="10" fill="none" stroke="currentColor" stroke-width="2"/><path d="M2 12h20M12 2c3 3 3 17 0 20M12 2c-3 3-3 17 0 20" fill="none" stroke="currentColor" stroke-width="2"/></svg>
          www.dernilo.co.uk
        </div>
      </div>
    </div>
    <div class="address-line">
      <svg width="8" height="11" viewBox="0 0 16 22"><path d="M8 1a7 7 0 0 1 7 7c0 5-7 13-7 13S1 13 1 8a7 7 0 0 1 7-7z" fill="none" stroke="var(--green)" stroke-width="2"/><circle cx="8" cy="8" r="2.5" fill="none" stroke="var(--green)" stroke-width="2"/></svg>
      <span>14 Calder Mews, Edinburgh EH11 2QX</span>
      <svg width="12" height="9" viewBox="0 0 24 18" style="margin-left:6px"><rect x="1" y="1" width="22" height="16" fill="none" stroke="var(--green)" stroke-width="2"/><path d="M1 1l11 9 11-9" fill="none" stroke="var(--green)" stroke-width="2"/></svg>
      <span>enquiries@dernilo.co.uk</span>
    </div>
  </footer>
</section>

</body>
</html>
```